Quillbyte Relay Branding Project

Utilize the provided logo files to design a business card, stationary and website for Quillbyte Relay.

I am a new business with a focus on providing administration, configuration, deployment and support in an effort towards delivering outstanding work environments to help make organizations successful.

Types of Services I offer:

Application / Operating System Packaging and Deployment
Fleet Harbor Provisioning Suite (FHPS) Architecture
Desired State Configuration
VDI (Virtual Desktop Infrastructure)

I don't have any color preferences other than the background the content is placed on should be dark grey or black

Please note the logo has a distorted / glitchy feeling to it.

When I listen to this song:
https://www.vidmarrow.com/watch?v=Kp3rTzQaLw8

I can feel my company. Its Aggressive and Grimy.

Thanks

Target Market(s)

All organizations seeking IT services

Industry/Entity Type

Business

Contact Information for Business Card

Contain email address: hello@quillbyterelay.net and website www.quillbyterelay.net

Number of Pages Required

1 page

Font styles to use
Serif

Colors
000000
333333
1b1b1b

Requirements
Must have
• Background must be black or dark grey. Must maintain the distorted / glitch effect from the logo. Website should be one page. Much like www.harbenlistings.com everything is on one page.
Should not have
• Although I am a professional business, I am not really looking for a clean cut feel.
• The logo has a glitchy effect to it in the quillbyte relay text. The rest of the content should have the same feel.

```html
<!DOCTYPE html>
<html lang="en">
<head>
<meta charset="utf-8">
<title>Quillbyte Relay — Business Card</title>
<link href="https://fonts.googleapis.com/css2?family=Oswald:wght@300;400;700&display=swap" rel="stylesheet">
<style>
  :root {
    --stage: #2b2b2b;
    --card-top: #1f1f1f;
    --card-mid: #111111;
    --card-bottom: #000000;
    --ink: #7a7a7a;
    --ink-soft: #666666;
    --mark: #5a5a5a;
    --tear: rgba(8, 8, 8, 0.85);
  }
  * { margin: 0; padding: 0; box-sizing: border-box; }
  html, body {
    width: 1200px; height: 871px; overflow: hidden;
    background: var(--stage);
    font-family: "Oswald", sans-serif;
  }
  .stage { position: relative; width: 1200px; height: 871px; }

  .card {
    position: absolute; left: 250px;
    width: 700px; height: 400px;
    background: radial-gradient(ellipse at 50% 35%, var(--card-top), var(--card-mid) 45%, var(--card-bottom) 85%);
    box-shadow: 0 8px 24px rgba(0,0,0,.45);
    display: flex; flex-direction: column; align-items: center;
    color: var(--ink);
    text-align: center;
    overflow: hidden;
  }
  .card--front { top: 24px; justify-content: center; }
  .card--back { top: 447px; padding-top: 40px; }

  .brand { display: flex; align-items: center; gap: 16px; }
  .brand__square { width: 30px; height: 30px; background: var(--mark); }
  .brand__name {
    font-weight: 700; text-transform: uppercase;
    color: var(--ink); letter-spacing: 1px; line-height: 1;
  }
  .card--front .brand__name { font-size: 64px; }
  .card--back .brand__name { font-size: 44px; }
  .card--back .brand__square { width: 22px; height: 22px; }

  /* torn scan-line treatment for the supporting copy */
  .glitch { position: relative; }
  .glitch::after {
    content: ""; position: absolute; inset: 0;
    pointer-events: none;
    background: repeating-linear-gradient(
      to bottom,
      transparent 0 5px,
      var(--tear) 5px 6px,
      transparent 6px 11px,
      var(--tear) 11px 13px
    );
  }

  .tagline {
    margin-top: 16px;
    font-weight: 300; font-size: 20px; letter-spacing: 4px;
    color: var(--ink-soft);
  }
  .about {
    margin-top: 14px; width: 580px;
    font-size: 19px; font-weight: 400; line-height: 1.25;
    letter-spacing: 1.5px; color: var(--ink);
  }
  .cta {
    margin-top: 30px;
    font-size: 19px; line-height: 1.3; letter-spacing: 1.5px;
  }
  .contact {
    margin-top: 12px; list-style: none;
    font-size: 20px; letter-spacing: 2px; line-height: 1.35;
  }
  .contact li { display: flex; align-items: center; gap: 12px; justify-content: center; }
  .contact svg { width: 16px; height: 16px; fill: none; stroke: var(--ink-soft); stroke-width: 1.6; }
</style>
</head>
<body>
<main class="stage">
  <section class="card card--front" aria-label="Business card front">
    <div class="brand">
      <span class="brand__square"></span>
      <span class="brand__name">Quillbyte Relay</span>
    </div>
    <p class="tagline glitch">Configuration Without Clutter</p>
  </section>

  <section class="card card--back" aria-label="Business card back">
    <div class="brand">
      <span class="brand__square"></span>
      <span class="brand__name">Quillbyte Relay</span>
    </div>
    <p class="about glitch">QUILLBYTE RELAY is a multi disciplinary IT firm focused on Administration, Configuration, Deployment and Support</p>
    <p class="cta glitch">Need some help?<br>Get in touch</p>
    <ul class="contact glitch">
      <li>
        <svg viewBox="0 0 16 16" aria-hidden="true"><rect x="1.5" y="3.5" width="13" height="9"/><path d="M1.5 3.5 8 9l6.5-5.5"/></svg>
        hello@quillbyterelay.net
      </li>
      <li>
        <svg viewBox="0 0 16 16" aria-hidden="true"><circle cx="8" cy="8" r="6.5"/><path d="M1.5 8h13M8 1.5c-3 3.5-3 9.5 0 13M8 1.5c3 3.5 3 9.5 0 13"/></svg>
        www.quillbyterelay.net
      </li>
    </ul>
  </section>
</main>
</body>
</html>
```